Savour and Thrive Wellbeing is being Launched and needs a business card and stationery package

I need a stationery package including business card (primary focus) , letterhead, digital letterhead, envelopes, with compliments slip, A 5 note sheet for the rebranding of my business and launch of my new website. I have a logo, like beige, brown earthy tones with a hint of red. I would also like the option of my letterhead also being printed on recycled paper in another format as well as the traditional letterhead. I do also send my letters to GPs and specialists digitally as well. I like to stand out from the usual stereotype of fruits and vegetables on business cards as I find that quite tacky and stereotypical. I want the business card to capture the essence of my logo as natural, nutrition, enjoyment, nurturing and freedom with food. I have attached the logo, and additional brief sheet on my ideas. Happy to have any background that is complementary to my theme, and what you believe would be catching. Definitely DONT'T like pink, try to pick up the darker colour in the logo please. and think too much black is a little overpowering.

Target Market(s)

clients who are interested in improving their health and wellness. Client 80% females; 20% males

Industry/Entity Type

Health And Wellness

Contact Information for Business Card

I am open to having different backgrounds as well that would complement the logo. Probably less emphasis on the heart out of the logo - just happy to keep that in the logo only please
I am also wanting two business cards - one for the appointments, one for general distribution and media distribution (both need to look consistent though) - but does give opportunity for one of the business cards to be less wordy and more striking. And the front of the business card can certainly stand out with the entire savour and thrive logo and my name and grab the attention of the receiver.
1st business card
on front:
Lorena Whitcombe
Savour and Thrive Wellbeing & logo
Nutritionist and Dietitian
Tarvel Medical Centre
647 Brindle Hill Rd, Quorrel Q 4987
Phone: (07) 3017 2968 Fax: (07) 3156 7209
Mobile: 0400 261 937
www.savourandthrivewellbeing.example.au
lorena@savourandthrivewellbeing.example.au
on back:
next appointment

……………………….. at ……………………… (possibly 4 times)
If you are unable to keep your appointment, please contact us as soon as possible (small font)
2nd business card (needs to be very eye catching and stand out)
on front: Savour and Thrive Wellbeing logo and my name
on back:
Lorena Whitcombe
address
phones, fax, website, email address

Font styles to use
Other font styles liked:
• please refer to logo

Requirements
Must have
• refreshing and simple; new and vibrant - I am rebranding my business after 20 years
• to get a feel of what is the theme - go to my new website (not completed as yet - but you will get a preliminary view) - don't do as google search as blocked - but can put into website header and it will be shown
• www.savourandthrivewellbeing.example.au - but please ignore the colouring of the 4 blocks under the slider on the home page - I am not wanting these colourings - they are getting updated.
Nice to have
• earthy tones, beige, hint of red, fonts to match logo if possible, organic, modern
• get inspiration from my logo please, open to having other backgrounds that complement
Should not have
• no food shots or stereotypical weight/ scales images
• no green, yellow or orange

```html
<!DOCTYPE html>
<html lang="en">
<head>
<meta charset="utf-8">
<title>Savour and Thrive Wellbeing – Business Card</title>
<link rel="stylesheet" href="https://fonts.googleapis.com/css2?family=Lobster+Two:wght@700&family=Roboto+Condensed:ital,wght@0,300;0,400;1,300;1,400&display=swap">
<style>
  :root {
    --backdrop: #e7e3de;
    --card: #f2f1ef;
    --ink: #3b3a3c;
    --ink-soft: #4a4a4c;
    --wine: #a73a5c;
    --band: #3a3138;
    --band-text: #f4f2f3;
    --rule: #b9b6b4;
  }
  * { box-sizing: border-box; margin: 0; padding: 0; }
  html, body { width: 1200px; height: 987px; overflow: hidden; }
  body {
    background: var(--backdrop);
    font-family: "Roboto Condensed", "Arial Narrow", sans-serif;
    color: var(--ink);
    position: relative;
  }
  .card {
    position: absolute;
    left: 292px;
    width: 616px;
    height: 351px;
    background: var(--card);
    box-shadow: 0 3px 10px rgba(0,0,0,0.18);
    overflow: hidden;
  }
  .card--front { top: 129px; }
  .card--back { top: 505px; }

  /* front */
  .brand {
    position: absolute;
    left: 24px; width: 262px;
    top: 118px;
    text-align: center;
  }
  .brand__dot {
    display: block;
    width: 34px; height: 34px;
    margin: 0 auto 14px;
    border-radius: 50%;
    background: var(--wine);
  }
  .brand__name {
    font-size: 24px;
    font-weight: 400;
    line-height: 1.2;
    color: var(--ink);
  }
  .divider {
    position: absolute;
    left: 296px; top: 58px;
    width: 1px; height: 214px;
    background: var(--rule);
  }
  .details {
    position: absolute;
    left: 318px; top: 50px;
    right: 10px;
  }
  .details__name {
    font-family: "Lobster Two", cursive;
    font-size: 23px;
    color: var(--ink);
    line-height: 1.1;
  }
  .details__role {
    font-size: 16px;
    color: var(--wine);
    margin-top: 3px;
  }
  .details__address {
    font-size: 16px;
    line-height: 21.5px;
    color: var(--ink-soft);
    margin-top: 16px;
  }
  .contact { list-style: none; margin-top: 12px; }
  .contact__item {
    display: flex;
    align-items: center;
    font-size: 16px;
    line-height: 23.5px;
    color: var(--ink-soft);
    white-space: nowrap;
  }
  .contact__item--email { font-size: 13.5px; }
  .contact__icon {
    width: 14px; height: 14px;
    margin-right: 10px;
    flex: none;
    fill: var(--ink);
  }
  .band-rule {
    position: absolute;
    left: 0; right: 0; top: 316px;
    height: 2px;
    background: var(--wine);
  }
  .band {
    position: absolute;
    left: 0; right: 0; top: 320px; bottom: 0;
    background: var(--band);
    color: var(--band-text);
    font-style: italic;
    font-size: 16px;
    letter-spacing: 1.4px;
    text-align: center;
    line-height: 31px;
  }

  /* back */
  .appt__title {
    position: absolute;
    left: 33px; top: 54px;
    font-size: 20px;
    color: var(--wine);
    letter-spacing: 0.3px;
  }
  .appt__mark {
    position: absolute;
    right: 34px; top: 36px;
    display: flex; align-items: center; gap: 8px;
    font-size: 15px;
    color: var(--wine);
  }
  .appt__mark-dot {
    width: 20px; height: 20px;
    border-radius: 50%;
    background: var(--wine);
  }
  .appt__list { list-style: none; }
  .appt__row {
    position: absolute;
    left: 33px; width: 551px;
    display: flex; align-items: flex-end;
    font-size: 16px;
    color: var(--ink);
  }
  .appt__row:nth-child(1) { top: 108px; }
  .appt__row:nth-child(2) { top: 157px; }
  .appt__row:nth-child(3) { top: 206px; }
  .appt__row:nth-child(4) { top: 255px; }
  .appt__blank {
    height: 14px;
    border-bottom: 1px dotted var(--ink-soft);
  }
  .appt__blank--date { width: 275px; }
  .appt__blank--time { flex: 1; }
  .appt__at { padding: 0 4px; line-height: 16px; }
  .appt__note {
    position: absolute;
    left: 0; right: 0; top: 306px;
    text-align: center;
    font-style: italic;
    font-size: 13px;
    color: var(--ink-soft);
  }
</style>
</head>
<body>

<section class="card card--front" aria-label="Business card front">
  <div class="brand">
    <span class="brand__dot"></span>
    <p class="brand__name">Savour and Thrive<br>Wellbeing</p>
  </div>

  <div class="divider"></div>

  <div class="details">
    <h1 class="details__name">Lorena Whitcombe</h1>
    <p class="details__role">Nutritionist and Dietitian</p>
    <p class="details__address">Tarvel Medical Centre<br>647 Brindle Hill Rd<br>Quorrel Q 4987</p>
    <ul class="contact">
      <li class="contact__item">
        <svg class="contact__icon" viewBox="0 0 24 24" aria-label="Phone"><path d="M6.6 10.8a15.1 15.1 0 0 0 6.6 6.6l2.2-2.2a1 1 0 0 1 1-.25 11.4 11.4 0 0 0 3.6.57 1 1 0 0 1 1 1V20a1 1 0 0 1-1 1A17 17 0 0 1 3 4a1 1 0 0 1 1-1h3.5a1 1 0 0 1 1 1c0 1.25.2 2.46.57 3.6a1 1 0 0 1-.25 1z"/></svg>
        (07) 3017 2968
      </li>
      <li class="contact__item">
        <svg class="contact__icon" viewBox="0 0 24 24" aria-label="Fax"><path d="M6 2h10l2 2v5H6z"/><path d="M3 10h18a1 1 0 0 1 1 1v7H2v-7a1 1 0 0 1 1-1zm2 4h14v2H5z"/><rect x="2" y="19" width="20" height="3"/></svg>
        (07) 3156 7209
      </li>
      <li class="contact__item">
        <svg class="contact__icon" viewBox="0 0 24 24" aria-label="Mobile"><path d="M7 1h10a2 2 0 0 1 2 2v18a2 2 0 0 1-2 2H7a2 2 0 0 1-2-2V3a2 2 0 0 1 2-2zm0 3v15h10V4z"/></svg>
        0400 261 937
      </li>
      <li class="contact__item contact__item--email">
        <svg class="contact__icon" viewBox="0 0 24 24" aria-label="Email"><path d="M2 5h20v14H2zm2 2v.4l8 5.2 8-5.2V7zm0 2.8V17h16V9.8l-8 5.2z"/></svg>
        lorena@savourandthrivewellbeing.example.au
      </li>
    </ul>
  </div>

  <div class="band-rule"></div>
  <p class="band">www.savourandthrivewellbeing.example.au</p>
</section>

<section class="card card--back" aria-label="Business card back">
  <h2 class="appt__title">NEXT APPOINTMENT</h2>
  <div class="appt__mark"><span class="appt__mark-dot"></span>Savour and Thrive</div>
  <ul class="appt__list">
    <li class="appt__row"><span class="appt__blank appt__blank--date"></span><span class="appt__at">at</span><span class="appt__blank appt__blank--time"></span></li>
    <li class="appt__row"><span class="appt__blank appt__blank--date"></span><span class="appt__at">at</span><span class="appt__blank appt__blank--time"></span></li>
    <li class="appt__row"><span class="appt__blank appt__blank--date"></span><span class="appt__at">at</span><span class="appt__blank appt__blank--time"></span></li>
    <li class="appt__row"><span class="appt__blank appt__blank--date"></span><span class="appt__at">at</span><span class="appt__blank appt__blank--time"></span></li>
  </ul>
  <p class="appt__note">If you are unable to keep your appointment, please contact us as soon as possible</p>
</section>

</body>
</html>
```